Plumbing company needs Business Card Design

Hi I need business card design based on logo which I uploaded. Its plumbing and heating company called Kranex Usługi Hydrauliczno-Gazowe. I want to see on my card motto of my company which is "...od wymiany uszczelki po wymiane łazienki.", my phone number, name, and website: 617248390, Marek Kowalczyk, info@kranex.org, www.kranex.org
I want to see logos of companys which I'm approved installer (Termolux) (La Valmont) (Corvo) (Pluma).
I want new creative look of business card. I like rounded corners.
Any questions please send message.
Thanks for intrest.
Business
Contact Information for Business Card
Marek Kowalczyk
617 248 390
info@kranex.org
www.kranex.org
...od wymiany uszczelki po wymiane łazienki.

```html
<!DOCTYPE html>
<html lang="pl">
<head>
<meta charset="utf-8">
<title>Kranex – wizytówka</title>
<link href="https://fonts.googleapis.com/css2?family=Oswald:wght@400;500;600;700&display=swap" rel="stylesheet">
<style>
  :root {
    --red: #e52228;
    --yellow: #f6ec23;
    --navy: #1f3d86;
    --white: #ffffff;
    --stage-light: #5a5a5a;
    --stage-dark: #222222;
  }
  * { margin: 0; padding: 0; box-sizing: border-box; }
  html, body { width: 1200px; height: 900px; overflow: hidden; }
  body {
    background: radial-gradient(ellipse at 50% 30%, var(--stage-light), var(--stage-dark));
    font-family: "Oswald", "Arial Narrow", sans-serif;
    position: relative;
  }
  .card {
    position: absolute;
    width: 362px;
    height: 362px;
    border-radius: 40px;
    overflow: hidden;
  }
  /* Front side */
  .card-front { left: 199px; top: 269px; background: var(--red); }
  .front-panel {
    position: absolute;
    inset: 18px;
    background: var(--yellow);
    border-radius: 28px;
    display: flex;
    align-items: center;
    justify-content: center;
  }
  .front-name {
    font-size: 92px;
    font-weight: 700;
    color: var(--navy);
    letter-spacing: 1px;
  }
  /* Back side */
  .card-back { left: 639px; top: 269px; background: var(--white); }
  .name-row { position: absolute; left: 0; top: 0; height: 62px; width: 100%; display: flex; align-items: center; }
  .first-name {
    background: var(--red);
    color: var(--white);
    height: 62px;
    width: 96px;
    display: flex;
    align-items: center;
    justify-content: center;
    padding-top: 14px;
    font-size: 23px;
    font-weight: 600;
  }
  .last-name {
    color: var(--navy);
    font-size: 25px;
    font-weight: 500;
    padding: 14px 0 0 10px;
  }
  .contact-band {
    position: absolute;
    left: 0; top: 76px; width: 100%; height: 22px;
    background: var(--yellow);
    text-align: right;
    padding-right: 22px;
    font-size: 14px;
    font-weight: 600;
    line-height: 22px;
    color: var(--navy);
    font-variant: small-caps;
  }
  .brand {
    position: absolute;
    left: 28px; top: 134px;
    display: flex;
    align-items: center;
    gap: 8px;
  }
  .brand-square {
    width: 92px; height: 92px;
    border: 7px solid var(--red);
    border-radius: 14px;
    background: var(--yellow);
  }
  .brand-text { display: flex; flex-direction: column; }
  .brand-name {
    color: var(--red);
    font-size: 52px;
    font-weight: 700;
    line-height: 1;
  }
  .brand-service {
    color: var(--navy);
    font-size: 16px;
    font-weight: 500;
    margin-top: 4px;
  }
  .motto {
    position: absolute;
    left: 0; top: 244px; width: 100%;
    text-align: center;
    color: var(--red);
    font-size: 12.5px;
    font-weight: 600;
  }
  .web-band {
    position: absolute;
    left: 0; bottom: 0; width: 100%; height: 62px;
    background: var(--red);
    color: var(--white);
    text-align: center;
    font-size: 21px;
    font-weight: 600;
    line-height: 52px;
    letter-spacing: 1px;
  }
</style>
</head>
<body>
  <section class="card card-front" aria-label="Przód wizytówki">
    <div class="front-panel">
      <span class="front-name">Kranex</span>
    </div>
  </section>

  <section class="card card-back" aria-label="Tył wizytówki">
    <div class="name-row">
      <span class="first-name">MAREK</span>
      <span class="last-name">KOWALCZYK</span>
    </div>
    <div class="contact-band">617.248.390 / info@kranex.org</div>
    <div class="brand">
      <span class="brand-square" aria-hidden="true"></span>
      <div class="brand-text">
        <span class="brand-name">Kranex</span>
        <span class="brand-service">Usługi Hydrauliczno-Gazowe</span>
      </div>
    </div>
    <p class="motto">OD WYMIANY USZCZELKI PO WYMIANE ŁAZIENKI</p>
    <div class="web-band">WWW.KRANEX.ORG</div>
  </section>
</body>
</html>
```